VALUE Book Cover Design for New Sales Book

We need a book cover designed for an upcoming book
Colors should be RED - BLACK - WHITE
A sample of our CURRENT BOOK cover (which we like) is attached
We need ideas for an "icon" or "meme" style design for the cover SIMILAR to the examples provided and attached
We need an "icon" that suggests VALUE-- we'd like the "icon" to be somewhat abstract vs using scales or anything "obvious"-- but the icon should still speak to and demonstrate what VALUE is.

Target Market(s)

Sales Directors and CEO's of large sales organizations and small businesses

Industry/Entity Type

Sales, Consulting,

Font styles to use
Sans Serif

Colors

Designer to choose colors to be used in the design.

Requirements
Must have
• Must be clean - contemporary and professional
Should not have
• should not have photos

```html
<!DOCTYPE html>
<html lang="en">
<head>
<meta charset="utf-8">
<title>Winning Worth – Book Cover</title>
<link rel="stylesheet" href="https://fonts.googleapis.com/css2?family=Montserrat:wght@400;700;800;900&display=swap">
<style>
  :root {
    --page-bg: #f3f3f3;
    --cover-red: #d41b1e;
    --cover-red-light: #e03a3c;
    --ink-white: #eceef3;
    --ink-black: #1c1c1c;
  }
  * { margin: 0; padding: 0; box-sizing: border-box; }
  html, body {
    width: 1200px;
    height: 1200px;
    overflow: hidden;
    background: var(--page-bg);
  }
  .canvas {
    position: relative;
    width: 1200px;
    height: 1200px;
  }
  .cover {
    position: absolute;
    left: 300px;
    top: 150px;
    width: 600px;
    height: 900px;
    background: linear-gradient(100deg, var(--cover-red-light) 0%, var(--cover-red) 45%, var(--cover-red) 100%);
    font-family: "Montserrat", sans-serif;
    color: var(--ink-white);
    overflow: hidden;
  }
  .title {
    position: absolute;
    left: 90px;
    top: 118px;
    font-weight: 900;
    font-size: 100px;
    line-height: 100px;
    letter-spacing: -0.05em;
  }
  .title-line { display: block; height: 104px; }
  .growth-marker {
    position: absolute;
    left: 216px;
    top: 350px;
    width: 17px;
    height: 440px;
  }
  .growth-marker polygon,
  .growth-marker rect { fill: var(--ink-black); }
  .subtitle {
    position: absolute;
    left: 250px;
    top: 506px;
    font-size: 20px;
    line-height: 24px;
    font-weight: 400;
    letter-spacing: -0.02em;
  }
  .subtitle strong { font-weight: 700; }
  .author {
    position: absolute;
    left: 100px;
    top: 808px;
    font-size: 37px;
    font-weight: 800;
    letter-spacing: -0.05em;
    white-space: nowrap;
  }
</style>
</head>
<body>
  <main class="canvas">
    <section class="cover" aria-label="Book cover: Winning Worth">
      <h1 class="title">
        <span class="title-line">WINNING</span>
        <span class="title-line">WORTH</span>
      </h1>
      <svg class="growth-marker" viewBox="0 0 17 440" aria-hidden="true">
        <polygon points="8.5,0 17,16 0,16"/>
        <rect x="7" y="16" width="3" height="424"/>
      </svg>
      <p class="subtitle">How to Close More<br>Deals at<br><strong>Better Margins</strong> ?</p>
      <p class="author">DANIEL HARWICK, PH. D</p>
    </section>
  </main>
</body>
</html>
```